Roles On Ledger - Job Board for Big Data Professionals

Hi all,

I need a design for a job board I'm kicking off that is focused on finding jobs and people that work in Data Analytics.

I've attached a fairly in depth design spec and wireframe giving a rough mockup. Please note that in the wireframe, the boxes are there to demonstrate orders of content. This is not to say that a lot of distinct content boxes will necessarily be the best way of presenting content.

I will be available on Chatterly (marcus.holloway) and email (h0ll0w4y@quillpost.net) and will give constant and clear feedback on the way.

Payment is not guaranteed yet. As soon as there are at least 5+ promising designs I will make this guaranteed.

Thanks
Marcus
Updates

Hi all

Please suspend all work on this project for the time being.

I am working closely with 1 designer who I will very likely accept their design.

I appreciate all the work you have put into this, but dont want to waste any more of your time.

Thanks
Marcus

Industry/Entity Type

Work

Requirements
Must have
• I'd like a clean, modern web design which has strong use of Typography. Strong use of a clear and consistent palette of colours.
Should not have
• Boxes with rounded edges

```html
<!DOCTYPE html>
<html lang="en">
<head>
<meta charset="utf-8">
<title>Holloway – Roles On Ledger</title>
<link href="https://fonts.googleapis.com/css2?family=Arimo:wght@400;700&display=swap" rel="stylesheet">
<style>
:root{
  --navy:#0d1f4c;
  --navy-deep:#0a1a40;
  --tab-top:#3676b4;
  --tab-bot:#1b4e8a;
  --orange:#f0a023;
  --bar-top:#2a68a6;
  --bar-bot:#123f78;
  --pale:#d8e6f1;
  --ink:#1d1d1d;
  --ink-soft:#333;
  --rule:#c9cfd6;
  --white:#fff;
}
*{box-sizing:border-box;margin:0;padding:0}
html,body{width:1097px;height:1200px;overflow:hidden}
body{position:relative;background:var(--white);font-family:"Arimo",Arial,sans-serif;color:var(--ink)}
.abs{position:absolute}
a{color:inherit;text-decoration:none}

.masthead{left:0;top:0;width:1097px;height:163px;background:var(--navy)}
.brand{left:156px;top:42px;font-size:27px;color:var(--white);letter-spacing:.5px}
.promo{left:354px;top:19px;width:614px;height:79px;display:flex;background:#8cc63e}
.promo-photo{width:260px;height:79px;background:linear-gradient(90deg,#d8d2b4,#a7b37a 60%,#8cc63e)}
.promo-text{padding:26px 0 0 14px;color:#fff;font-size:13px;letter-spacing:.6px;line-height:17px;position:relative;flex:1}
.promo-text .date{color:#5b7a28}
.promo-text .cta{position:absolute;right:2px;bottom:6px;font-size:8px;font-weight:700}
.promo-text .promo-name{position:absolute;left:-190px;top:24px;font-size:26px;color:#fff}

.main-nav{left:0;top:130px;width:1097px;height:33px}
.main-nav a{position:absolute;top:0;height:33px;line-height:34px;text-align:center;color:var(--white);font-size:13px;background:linear-gradient(var(--tab-top),var(--tab-bot))}
.main-nav a.current{background:var(--orange)}

.sub-nav{left:0;top:163px;width:1097px;height:35px;background:var(--orange);font-size:10px;color:var(--white)}
.sub-nav span{position:absolute;top:14px}
.sub-nav b{color:var(--navy-deep);font-size:11px;margin-right:8px}
.sub-nav .divider{top:7px;width:1px;height:22px;background:#fbd79a}

.panel-head{height:20px;line-height:20px;color:var(--white);font-size:11px;padding-left:11px;background:linear-gradient(var(--bar-top),var(--bar-bot))}
.panel-head.warm{background:var(--orange);color:var(--navy-deep)}
.pale{background:var(--pale)}
.field{background:var(--white);height:18px;position:absolute}
.btn{position:absolute;height:20px;line-height:20px;color:#fff;font-size:11px;text-align:center;background:linear-gradient(var(--bar-top),var(--bar-bot))}
.label{position:absolute;font-size:11px;color:#333}

.bullets{list-style:none}
.bullets li{position:relative;padding-left:24px;font-size:11px;line-height:16px;color:var(--ink)}
.bullets li::before{content:"";position:absolute;left:0;top:4px;width:7px;height:7px;background:#333}
.categories li{margin-bottom:0.5px}

.job{position:absolute;left:141px;width:368px;font-size:11px;line-height:16px}
.job h4{font-size:11px;color:var(--navy-deep)}
.job p{color:var(--ink-soft)}

.news{list-style:none;font-size:9.5px;line-height:15.5px}
.news li{border-bottom:1px solid var(--rule);padding:3px 0 3px 4px}

.why h5{font-size:11px;margin:0 0 10px}
.why .bullets li{font-size:9.5px;line-height:18px;padding-left:14px}
.why .bullets li::before{top:6px}

.tile{position:absolute;left:822px;width:146px;height:56px;background:linear-gradient(#3a7dbd,#164b86);color:#fff;font-size:13px;border-bottom:2px solid #0e3564}
.tile .glyph{position:absolute;left:8px;top:9px;width:34px;height:38px;background:linear-gradient(#e6ecf2,#9fb2c6)}
.tile .txt{position:absolute;left:52px}
.tile .chev{position:absolute;right:10px;bottom:4px;color:#5c8fc4;font-size:16px;font-weight:700}

.social{position:absolute;top:560px;width:50px;height:50px;color:#fff;font-size:9px;text-align:center;line-height:50px}

.partner{position:relative;margin-top:9px;width:256px;height:214px;background:linear-gradient(150deg,#123a52,#1f6f8e 55%,#0f3148);overflow:hidden}
.partner-title{left:20px;top:18px;font-size:22px;font-weight:700;color:#fff;white-space:nowrap;letter-spacing:-.3px}
.partner-tag{left:92px;top:56px;font-size:12px;color:#fff;line-height:15px;white-space:nowrap}

.footer{left:0;top:1040px;width:1097px;height:160px;background:var(--navy);color:var(--white)}
.foot-nav{position:absolute;top:18px;left:0;width:1097px;text-align:center;font-size:11px}
.foot-col{position:absolute;top:47px;height:79px;border-left:1px solid #5a6a8e;padding-left:12px;font-size:9.5px;line-height:21.5px}
.foot-col h6{font-size:11px;font-weight:400;line-height:14px;margin-bottom:6px}
.copy{position:absolute;top:145px;width:1097px;text-align:center;font-size:8px}
</style>
</head>
<body>

<header class="abs masthead">
  <div class="abs brand">Holloway</div>
  <div class="abs promo">
    <div class="promo-photo" role="img" aria-label="Promotional photo of a bright home interior"></div>
    <div class="promo-text">
      <span class="promo-name">Hearthside</span>
      THE DOOR IS OPEN… <small>AND YOU'RE INVITED.</small><br>
      <span class="date">APRIL 17 – DECEMBER 18, 2009</span>
      <span class="cta">CLICK FOR DETAILS</span>
    </div>
  </div>
</header>

<nav class="abs main-nav">
  <a class="current" style="left:139px;width:92px">Home</a>
  <a style="left:233px;width:79px">Jobs</a>
  <a style="left:314px;width:96px">Account</a>
  <a style="left:412px;width:101px">Register</a>
  <a style="left:515px;width:142px">News &amp; Insight</a>
  <a style="left:659px;width:113px">Graduates</a>
  <a style="left:774px;width:112px">Recruiters</a>
  <a style="left:888px;width:72px">About</a>
</nav>

<nav class="abs sub-nav">
  <span style="left:157px"><b>Jobs</b>Advanced Job Search | Companies</span>
  <span class="divider" style="left:358px"></span>
  <span style="left:373px"><b>Account</b>Login | Post Resume | Alerts | Settings</span>
  <span class="divider" style="left:603px"></span>
  <span style="left:620px"><b>Recruiters</b>Login | Search Resumes | Advertising &amp; Branding Solutions</span>
</nav>

<section class="abs" style="left:128px;top:211px;width:408px">
  <div class="panel-head" style="padding-left:43px">Login</div>
  <div class="pale" style="height:82px;position:relative">
    <span class="label" style="left:26px;top:18px">Username :</span>
    <span class="label" style="left:178px;top:18px">Password :</span>
    <span class="field" style="left:26px;top:35px;width:145px"></span>
    <span class="field" style="left:178px;top:35px;width:139px"></span>
    <span class="btn" style="left:326px;top:34px;width:60px">Sign in</span>
  </div>
</section>

<section class="abs" style="left:128px;top:317px;width:408px">
  <div class="panel-head warm" style="padding-left:19px;height:22px;line-height:25px">Quick Search</div>
  <div class="pale" style="height:131px;position:relative">
    <div class="abs" role="img" aria-label="Photo of a professional at a desk in an office" style="left:0;top:0;width:130px;height:131px;background:linear-gradient(120deg,#8fa4b8,#e9e5de 55%,#c9d2da)"></div>
    <span class="label" style="left:131px;top:13px">Keywords</span>
    <span class="label" style="left:268px;top:13px">Loction</span>
    <span class="field" style="left:131px;top:30px;width:125px;height:14px"></span>
    <span class="field" style="left:266px;top:30px;width:125px;height:14px"></span>
    <svg class="abs" style="left:377px;top:31px" width="13" height="12"><rect width="13" height="12" fill="#c6d6ec"/><path d="M3 4l3.5 4 3.5-4" fill="none" stroke="#2a5a96" stroke-width="1.6"/></svg>
    <span class="label" style="left:267px;top:55px">Advance Search</span>
    <span class="field" style="left:266px;top:71px;width:125px;height:14px"></span>
    <span class="abs" style="left:378px;top:69px;font-size:13px;font-weight:700;color:#333">»</span>
    <span class="abs" style="left:132px;top:72px;width:9px;height:9px;background:#fff;border:1px solid #aaa"></span>
    <span class="label" style="left:149px;top:70px;color:#2a5a96">Type</span>
    <span class="btn" style="left:132px;top:89px;width:125px;height:19px;line-height:19px">Search</span>
  </div>
</section>

<section class="abs" style="left:128px;top:481px;width:408px">
  <div class="panel-head">List of job categories<span style="position:absolute;right:21px">Sponsored jobs</span></div>
  <ul class="bullets categories" style="margin:7px 0 0 13px;width:335px">
    <li>Lorem Ipsum is simply dummy text of the printing and typesetting industry.</li>
    <li>Lorem Ipsum is simply dummy text of the printing and type s etting industry.</li>
    <li>Lorem Ipsum is simply dummy text of the printing and typesetting industry.</li>
    <li>Lorem Ipsum is simply dummy text of the printing and typesetting industry.</li>
  </ul>
</section>

<section class="abs" style="left:128px;top:647px;width:408px">
  <div class="panel-head">Sponsored jobs</div>
</section>
<div class="abs" style="left:520px;top:683px;width:2px;height:321px;background:#3c4a66"></div>
<div class="abs" style="left:517px;top:693px;width:7px;height:27px;background:#1b4e8a"></div>
<article class="job" style="top:682px"><h4>Web Designer</h4><h4>Company Name, Location</h4><p>Lorem Ipsum is simply dummy text of the printing and typesetting industry. of the printing and industry.</p></article>
<article class="job" style="top:768px"><h4>Programer</h4><h4>Company Name, Location</h4><p>Lorem Ipsum is simply dummy text of the printing and typesetting industry. of the printing and industry.</p></article>
<article class="job" style="top:859px"><h4>HR</h4><h4>Company Name, Location</h4><p>Lorem Ipsum is simply dummy text of the printing and typesetting industry. of the printing and industry.</p></article>
<article class="job" style="top:942px"><h4>HR</h4><h4>Company Name, Location</h4><p>Lorem Ipsum is simply dummy text of the printing and typesetting industry. of the printing and industry.</p></article>

<section class="abs" style="left:551px;top:211px;width:256px">
  <div class="panel-head" style="padding-left:15px">Latest News &amp; Insight</div>
  <ul class="news" style="margin:6px 12px 0 10px;padding-right:14px">
    <li><b>Lorem Ipsum</b> is simply dummy text of the printing and typesetting industry.</li>
    <li><b>Lorem Ipsum</b> is simply dummy text of the printing and typesetting industry.</li>
    <li><b>Lorem Ipsum</b> is simply dummy text of the printing and typesetting industry.</li>
    <li><b>Lorem Ipsum</b> is simply dummy text of the printing and typesetting industry.</li>
    <li><b>Lorem Ipsum</b> is simply dummy text of the printing and typesetting industry.</li>
  </ul>
  <a style="position:absolute;left:175px;top:216px;font-size:9.5px;text-decoration:underline">More articles</a>
</section>

<section class="abs pale" style="left:551px;top:455px;width:256px;height:60px">
  <span class="label" style="left:14px;top:9px;font-weight:700;font-size:11px;color:#222">Job Alerts</span>
  <span class="field" style="left:34px;top:29px;width:155px;height:14px;font-size:7.5px;color:#777;padding:2px 8px">Enter email for job alerts</span>
  <span class="btn" style="left:191px;top:28px;width:31px;height:16px;line-height:16px;font-weight:700">Go</span>
</section>

<section class="abs why" style="left:551px;top:524px;width:256px">
  <div class="panel-head" style="padding-left:15px">Why RolesOnLedger?</div>
  <div class="pale" style="height:229px;position:relative;padding:10px 14px 0">
    <h5>Jobseekers</h5>
    <ul class="bullets"><li>Lorem Ipsum is simply dummy</li><li>Lorem Ipsum is simply dummy text</li><li>Lorem Ipsum is simply</li></ul>
    <span class="btn" style="left:159px;top:86px;width:74px;height:16px;line-height:16px;font-size:9.5px">Register to</span>
    <div class="abs" style="left:12px;top:110px;width:226px;height:1px;background:#f2f6fa"></div>
    <h5 style="margin-top:34px">Recruiters</h5>
    <ul class="bullets"><li>Lorem Ipsum is simply dummy</li><li>Lorem Ipsum is simply dummy text</li><li>Lorem Ipsum is simply</li></ul>
    <span class="btn" style="left:159px;top:199px;width:74px;height:16px;line-height:16px;font-size:9.5px">Register to</span>
  </div>
</section>

<section class="abs" style="left:551px;top:786px;width:256px">
  <h5 style="font-size:11px;padding-left:14px;color:#222">Featured Partner</h5>
  <div class="partner">
    <div class="abs" role="img" aria-label="Illustration of a white robot" style="left:10px;top:80px;width:78px;height:96px;background:linear-gradient(#dfe6ea,#8fa3ad)"></div>
    <div class="abs partner-title">Gearwise Robotics:</div>
    <div class="abs partner-tag">ENGINEERING FOR<br>TODAY &amp; TOMORROW</div>
    <div class="abs" style="left:10px;top:181px;font-size:11px;color:#7cd0ea;line-height:12px">Purchase the Gearwise<br>Robotics Curriculum!</div>
    <div class="abs" style="left:137px;top:180px;width:109px;height:24px;background:#2f9fc4;color:#fff;font-size:12px;font-weight:700;line-height:24px;padding-left:22px">LEARN MORE</div>
  </div>
</section>

<a class="tile" style="top:211px"><span class="glyph" role="img" aria-label="Resume document icon" style="width:26px"></span><span class="txt" style="top:14px;line-height:16px;font-size:14px;left:42px">Post<br>Resume</span><span class="chev" style="color:#f0a023;bottom:12px;font-size:22px">»</span></a>
<a class="tile" style="top:276px"><span class="glyph" role="img" aria-label="Login key icon"></span><span class="txt" style="top:17px;font-size:17px;left:60px">Login</span><span class="chev">»</span></a>
<a class="tile" style="top:343px"><span class="glyph" role="img" aria-label="Advertising board icon"></span><span class="txt" style="top:20px;font-size:14px">Advertise</span><span class="chev">»</span></a>
<a class="tile" style="top:411px"><span class="glyph" role="img" aria-label="Magnifier search icon" style="border-radius:50%;width:34px;height:34px"></span><span class="txt" style="top:16px;line-height:14px">Search<br>Resume</span><span class="chev">»</span></a>
<a class="tile" style="top:480px"><span class="glyph" role="img" aria-label="Graduation cap icon"></span><span class="txt" style="top:18px">Graduates</span><span class="chev">»</span></a>
<span class="social" style="left:830px;background:#3aa2cf">Chirpline</span>
<span class="social" style="left:903px;background:#e8762b">Feedway</span>

<footer class="abs footer">
  <div class="foot-nav">Home&nbsp; | &nbsp;Jobs&nbsp; | &nbsp;Account&nbsp; | &nbsp;Register&nbsp; | &nbsp;News &amp; Insight&nbsp; | &nbsp;Graduates&nbsp; | &nbsp;Recruiters&nbsp; | &nbsp;About</div>
  <div class="foot-col" style="left:308px"><h6>Jobs</h6>Advanced Job Search<br>Companies</div>
  <div class="foot-col" style="left:495px;padding-left:19px"><h6>Account</h6>Login<br>Post Resume<br>Alerts | Settings</div>
  <div class="foot-col" style="left:692px;padding-left:14px"><h6>Recruiters</h6>Login<br>Search Resumes<br>Advertising &amp; Branding Solutions</div>
  <div class="copy">All rights Reserved, Holloway 2012</div>
</footer>

</body>
</html>
```